A4 4-sided brochure - medical specialist

A4 sized, 4 sided brochure, glossy. I am a medical specialist (urologist) and need a brochure to hand out to GPs. I will write all text and will send photos. I have attached an example of the kind of thing I was thinking of. My website is https://www.harbourlinkclinic.com.au/
There are three of us in a group but the brochure is just for me.
It is to give to GPs and not direct to patients, so should tell the GPs why they should refer to me.
Target Market(s)
Medical
Industry/Entity Type
medicine - surgery - urology
Requirements
Must have
- I have uploaded an outline of the layout with files that are listed on the outline - please load them up as indicated and submit your designs
Should not have
- Claims that I am the best

```html
<!DOCTYPE html>
<html lang="en">
<head>
<meta charset="utf-8">
<title>Harbourlink Clinic – GP Brochure</title>
<link href="https://fonts.googleapis.com/css2?family=Montserrat:wght@300;400;500;600;700;800&display=swap" rel="stylesheet">
<style>
:root{
  --bg:#1f4a96;
  --page:#ffffff;
  --blue:#4a90d0;
  --ink:#3d3d3d;
  --grey:#6b6b6b;
  --stripe:#4b4f56;
  --photo-a:#d9d9d9;
  --photo-b:#9c9c9c;
}
*{margin:0;padding:0;box-sizing:border-box}
html,body{width:1200px;height:2243px;overflow:hidden}
body{background:var(--bg);font-family:'Montserrat',sans-serif;color:var(--ink);position:relative}
.page{position:absolute;width:560px;height:792px;background:var(--page);overflow:hidden;box-shadow:0 6px 18px rgba(0,0,0,.35)}
.page--cover{left:25px;top:314px}
.page--about{left:615px;top:314px}
.page--gps{left:25px;top:1136px}
.page--contact{left:615px;top:1136px}
.page svg.shapes{position:absolute;left:0;top:0;width:560px;height:792px}
.abs{position:absolute}
.brand{position:absolute;display:flex;align-items:center;gap:10px;left:0;right:0;justify-content:center}
.brand__mark{width:26px;height:26px;border-radius:50%;background:var(--blue)}
.brand__name{font-weight:500;font-size:27px;color:var(--ink);letter-spacing:-.3px}
.hero-title{color:#fff;line-height:1}
.hero-title .light{font-weight:400;font-size:26px;display:block}
.hero-title .mid{font-weight:500;font-size:39px;display:block;margin-top:4px}
.hero-title .bold{font-weight:700;font-size:32px;display:block;margin-top:4px}
.hero-rule{width:128px;height:2px;background:#fff}
.hero-url{color:#fff;font-size:13px;font-weight:400}
.doctor-name{color:var(--blue);font-weight:700;font-size:16px;text-align:center;left:0;right:0}
.doctor-rule{width:60px;height:2px;background:var(--blue);left:250px}
.address{font-size:12.5px;text-align:center;left:0;right:0;line-height:1.35;color:var(--ink)}
.about-title{color:#fff;line-height:1}
.about-title .light{font-weight:400;font-size:31px;display:block}
.about-title .bold{font-weight:700;font-size:55px;display:block;margin-top:4px;line-height:.95}
.body-copy{left:24px;right:30px;font-size:10.3px;line-height:1.42;color:var(--grey);text-align:justify}
.body-copy p+p{margin-top:12px}
.pill{left:24px;height:28px;border:1.5px solid var(--blue);border-radius:14px;display:flex;align-items:center;gap:6px;padding:0 10px 0 4px;color:var(--blue);font-weight:600;font-size:14px}
.pill__icon{width:20px;height:20px;border-radius:50%;background:var(--blue)}
.ticks{list-style:none;font-size:10.3px;line-height:18.5px;color:var(--grey)}
.ticks li::before{content:"✓";margin-right:8px;color:var(--grey);font-size:9px}
.ticks--blue{color:var(--blue);line-height:15.6px}
.footer{left:20px;right:20px;height:14px;display:flex;align-items:center;gap:8px}
.footer__num{width:14px;height:14px;background:var(--blue);color:#fff;font-size:7px;font-weight:600;display:flex;align-items:center;justify-content:center}
.footer__line{flex:1;height:1px;background:var(--blue)}
.footer__url{color:var(--blue);font-size:9px;letter-spacing:1.4px}
.urgent{right:26px;text-align:right;color:#fff;font-weight:500;font-size:37px;line-height:47px}
.urgent strong{font-weight:700;font-size:44px;display:block;margin-top:2px}
.gps-title{left:22px;color:var(--blue);font-weight:700;font-size:46px}
.col-head{display:flex;align-items:center;gap:6px;font-weight:600;font-size:11.3px;color:var(--ink);margin-bottom:4px}
.col-head__icon{width:14px;height:14px;border-radius:3px;background:var(--blue)}
.contact-title{left:0;right:0;text-align:center;font-size:35px;font-weight:600;color:var(--ink)}
.contact-title span{color:var(--blue);font-weight:700}
.contact-card{left:60px;right:0;text-align:center;color:#fff;font-size:12.6px;line-height:16px}
.contact-card h3{font-size:16px;font-weight:700;margin-bottom:24px}
.contact-card .label{font-weight:700;margin-top:18px}
.socials{display:flex;gap:12px;justify-content:center;margin-top:20px}
.socials span{width:26px;height:26px;border:1.5px solid #fff;border-radius:6px}
</style>
</head>
<body>

<section class="page page--cover">
  <svg class="shapes" viewBox="0 0 560 792">
    <defs>
      <linearGradient id="photoGrad" x1="0" y1="0" x2="1" y2="1">
        <stop offset="0" stop-color="var(--photo-a)"/><stop offset="1" stop-color="var(--photo-b)"/>
      </linearGradient>
    </defs>
    <rect role="img" aria-label="Photo of a smiling older couple" x="150" y="223" width="410" height="413" fill="url(#photoGrad)"/>
    <path d="M0 192 H238 Q283 192 283 237 V544 Q283 589 238 589 H0Z" fill="var(--blue)" opacity=".92"/>
    <path d="M0 212 H265 Q325 212 325 272 V520 Q325 575 270 575 H0" fill="none" stroke="#fff" stroke-width="1.5" opacity=".85"/>
    <path d="M560 405 H475 Q430 405 430 450 V520 Q430 565 475 565 H560" fill="none" stroke="var(--blue)" stroke-width="2"/>
    <line x1="455" y1="178" x2="505" y2="258" stroke="var(--stripe)" stroke-width="6"/>
    <line x1="476" y1="184" x2="526" y2="264" stroke="var(--blue)" stroke-width="6"/>
    <line x1="418" y1="622" x2="458" y2="688" stroke="var(--stripe)" stroke-width="6"/>
    <line x1="440" y1="630" x2="478" y2="694" stroke="var(--blue)" stroke-width="6"/>
  </svg>
  <div class="brand" style="top:98px"><span class="brand__mark"></span><span class="brand__name">Harbourlink Clinic</span></div>
  <h1 class="hero-title abs" style="left:24px;top:418px"><span class="light">Complex</span><span class="mid">Urological</span><span class="bold">Problems</span></h1>
  <div class="hero-rule abs" style="left:24px;top:537px"></div>
  <div class="hero-url abs" style="left:24px;top:545px">www.harbourlinkclinic.com.au</div>
  <div class="doctor-name abs" style="top:668px">A/Prof Daniel Hart – Urologist</div>
  <div class="doctor-rule abs" style="top:693px"></div>
  <div class="address abs" style="top:708px">Wattle Suites, Northgate Private Hospital,<br>42 Linden Tce, Port Halden 4521</div>
</section>

<section class="page page--about">
  <svg class="shapes" viewBox="0 0 560 792">
    <rect role="img" aria-label="Photo of the urologist in theatre scrubs beside surgical equipment" x="112" y="27" width="448" height="339" fill="url(#photoGrad)"/>
    <path d="M0 84 H246 Q291 84 291 129 V351 Q291 396 246 396 H0Z" fill="var(--blue)" opacity=".92"/>
    <path d="M0 177 H190 Q255 177 255 237 V335 Q255 383 208 383 H0" fill="none" stroke="#fff" stroke-width="1.5" opacity=".85"/>
    <line x1="38" y1="30" x2="85" y2="102" stroke="var(--stripe)" stroke-width="6"/>
    <line x1="58" y1="36" x2="105" y2="108" stroke="var(--blue)" stroke-width="6"/>
    <line x1="478" y1="340" x2="518" y2="404" stroke="var(--stripe)" stroke-width="6"/>
    <line x1="498" y1="346" x2="538" y2="410" stroke="var(--blue)" stroke-width="6"/>
  </svg>
  <h1 class="about-title abs" style="left:24px;top:205px"><span class="light">About</span><span class="bold">Daniel<br>Hart</span></h1>
  <div class="body-copy abs" style="top:410px">
    <p>A/Prof Daniel Hart is a consultant urologist with private practice at Northgate Private and Westfield Hospitals. Daniel consults at Port Halden, Eastvale, and Marlow Bay, and undertakes Day Case lists at Kestrel Point and Ridgeway. He is Associate Professor at Southern Coast University &amp; was senior staff specialist for 14 years at RGH.</p>
    <p>Daniel undertook a urological cancer fellowship at Riverside General Hospital in Lakemoor from 2008-2009, and was appointed as a consultant in Port Halden in 2009. He holds Fellowships of both the National (FNCS Urol) and Pacific (FPCS Urol) Colleges of Surgeons, a Doctor of Medicine higher degree by research (MD) and has extensive basic science training (Bachelor of Science and Master of Science degrees).</p>
  </div>
  <div class="pill abs" style="top:590px"><span class="pill__icon"></span>Professional Qualifications</div>
  <ul class="ticks abs" style="left:34px;top:632px">
    <li>Bachelor of Science (1st Class Hons) Kingsbridge University</li>
    <li>Master of Science, Ashmoor University</li>
    <li>Bachelor of Medicine, Ashmoor University</li>
    <li>Doctor of Medicine, Fenwick University</li>
    <li>Fellow of the National College of Surgeons (Urology)</li>
    <li>Fellow of the Pacific College of Surgeons (Urology)</li>
  </ul>
  <div class="footer abs" style="top:752px"><span class="footer__num">02</span><span class="footer__line"></span><span class="footer__url">www.harbourlinkclinic.com.au</span></div>
</section>

<section class="page page--gps">
  <svg class="shapes" viewBox="0 0 560 792">
    <rect role="img" aria-label="Photo of a smiling senior female doctor with a stethoscope" x="0" y="0" width="440" height="363" fill="url(#photoGrad)"/>
    <rect x="330" y="0" width="230" height="85" fill="#fff"/>
    <path d="M330 84 H560 V396 H310 Q272 396 282 355 L320 125 Q328 84 360 84Z" fill="var(--blue)" opacity=".95"/>
    <line x1="30" y1="5" x2="75" y2="75" stroke="var(--stripe)" stroke-width="6"/>
    <line x1="50" y1="10" x2="95" y2="80" stroke="var(--blue)" stroke-width="6"/>
    <line x1="455" y1="365" x2="495" y2="430" stroke="var(--stripe)" stroke-width="6"/>
    <line x1="476" y1="370" x2="516" y2="435" stroke="var(--blue)" stroke-width="6"/>
  </svg>
  <div class="urgent abs" style="top:112px">For<br>Urgent<br>Referrals<br>Call:<strong>8190 3377</strong></div>
  <div class="gps-title abs" style="top:392px">For GPs</div>
  <div class="abs" style="left:298px;top:428px">
    <div class="col-head"><span class="col-head__icon"></span>Make a Referral</div>
    <ul class="ticks ticks--blue" style="margin-left:4px"><li>GP Referral Form</li></ul>
  </div>
  <div class="abs" style="left:22px;top:482px">
    <div class="col-head"><span class="col-head__icon"></span>Help with Urology Problems</div>
    <ul class="ticks ticks--blue" style="margin-left:4px;margin-top:8px">
      <li>Epididymal Cysts</li><li>Epididymitis</li><li>Erectile Dysfunction</li><li>Haematospermia</li><li>Hydrocoele</li><li>Incontinence in Women</li><li>Inflammation of the Foreskin / Balanitis</li><li>Microscopic Haematuria</li><li>Nocturnal Incontinence</li><li>Paraphimosis/Foreskin Stuck Behind Glans</li><li>Penile Curvature</li>
    </ul>
  </div>
  <ul class="ticks ticks--blue abs" style="left:302px;top:506px">
    <li>Premature Ejaculation</li><li>Priapism</li><li>Retrograde Ejaculation</li><li>Screening for Prostate Cancer with PSA</li><li>Sterile Pyuria</li><li>Testosterone Deficiency / Hypogonadism</li><li>Tight Foreskin/Phimosis</li><li>Urethral Catheter Problems</li><li>Urinary Tract Infection in Men</li><li>Urinary Tract Infection in Women</li><li>Varicocoele (Adults)</li>
  </ul>
  <div class="abs" style="left:22px;top:700px">
    <div class="col-head"><span class="col-head__icon"></span>Urological Procedures</div>
    <ul class="ticks ticks--blue" style="margin-left:4px"><li>Urological Procedures</li></ul>
  </div>
  <div class="abs" style="left:298px;top:700px">
    <div class="col-head"><span class="col-head__icon"></span>Contact Harbourlink Clinic</div>
    <ul class="ticks ticks--blue" style="margin-left:4px"><li>Contact Harbourlink Clinic</li></ul>
  </div>
  <div class="footer abs" style="top:756px;flex-direction:row-reverse"><span class="footer__num">03</span><span class="footer__line"></span><span class="footer__url">www.harbourlinkclinic.com.au</span></div>
</section>

<section class="page page--contact">
  <svg class="shapes" viewBox="0 0 560 792">
    <defs>
      <linearGradient id="faintGrad" x1="0" y1="0" x2="1" y2="0">
        <stop offset="0" stop-color="#e2e2e2"/><stop offset="1" stop-color="#f2f2f2"/>
      </linearGradient>
    </defs>
    <rect role="img" aria-label="Faint photo of a smiling older couple" x="0" y="225" width="560" height="408" fill="url(#faintGrad)"/>
    <path d="M105 196 H560 V632 H120 Q70 632 70 582 V246 Q70 196 105 196Z" fill="var(--blue)" opacity=".92"/>
    <path d="M80 250 Q20 250 20 310 V560 Q20 620 80 620 H240" fill="none" stroke="#fff" stroke-width="1.5"/>
    <line x1="58" y1="140" x2="102" y2="210" stroke="var(--blue)" stroke-width="6"/>
    <line x1="78" y1="146" x2="122" y2="216" stroke="var(--stripe)" stroke-width="6"/>
    <line x1="468" y1="612" x2="508" y2="676" stroke="var(--blue)" stroke-width="6"/>
    <line x1="488" y1="618" x2="528" y2="682" stroke="var(--stripe)" stroke-width="6"/>
  </svg>
  <h2 class="contact-title abs" style="top:124px">Contact <span>Us:</span></h2>
  <div class="contact-card abs" style="top:274px">
    <h3>A/Prof Daniel Hart – Urologist</h3>
    <div>Wattle Suites, Northgate Private Hospital,<br>42 Linden Tce, Port Halden 4521</div>
    <div class="label">Tel:</div><div>0400 112358 or 0400 112359</div>
    <div class="label">Fax:</div><div>08 6100 2468</div>
    <div class="label">Email:</div><div>reception@danielhart.org<br>PO Box 118 Elmvale 4530</div>
    <div class="socials"><span></span><span></span><span></span></div>
  </div>
  <div class="brand" style="top:700px"><span class="brand__mark"></span><span class="brand__name" style="font-size:22px">Harbourlink Clinic</span></div>
</section>

</body>
</html>
```